Corvath Holdings, LLC

We are a design build general contracting company.
We work with commercial accounts and private developers. We build retail spaces, restaurants and housing projects.
Im looking for a clean professional type of logo incorporating a roman flavor, think ionic columns and pedestals.
Two toned colorway.
I like unusual fonts and Im not afraid to do something bold with the logo.
Contact Information for Business Card
Marisol Brenkowitz
318-472-9051 corvathmb@mailvexo.com
Font styles to use
Decorative
Colors
Designer to choose colors to be used in the design.
Requirements
Should not have
- I don't like reds pinks.

```html
<!DOCTYPE html>
<html lang="en">
<head>
<meta charset="utf-8">
<title>Corvath Holdings, LLC – Business Card</title>
<link rel="stylesheet" href="https://fonts.googleapis.com/css2?family=Michroma&family=Open+Sans:wght@400;600&display=swap">
<style>
  :root {
    --bg: #e9e9e6;
    --paper: #ffffff;
    --green: #5f9812;
    --navy: #143f6a;
    --ink: #2b2b2b;
    --rule: #b9b9b9;
    --grad-top: #67960c;
    --grad-bottom: #0f3b66;
  }
  * { box-sizing: border-box; margin: 0; padding: 0; }
  html, body { width: 1200px; height: 844px; overflow: hidden; }
  body {
    background: var(--bg);
    position: relative;
    font-family: "Open Sans", Arial, sans-serif;
  }
  .card {
    position: absolute;
    top: 279px;
    width: 500px;
    height: 286px;
    box-shadow: 0 2px 8px rgba(0,0,0,0.18);
  }
  .card-front { left: 60px; background: var(--paper); }
  .card-back {
    left: 640px;
    background: linear-gradient(160deg, var(--grad-top) 0%, #3f7424 45%, var(--grad-bottom) 100%);
    color: #fff;
  }

  .brand {
    position: absolute;
    top: 58px;
    right: 40px;
    display: flex;
    align-items: center;
    gap: 10px;
    font-family: "Michroma", Arial, sans-serif;
    font-size: 17px;
    color: var(--navy);
    text-transform: uppercase;
  }
  .brand-mark { width: 14px; height: 14px; background: var(--navy); }

  .rule { position: absolute; left: 40px; right: 40px; height: 1px; background: var(--rule); }
  .rule-top { top: 112px; }
  .rule-bottom { top: 222px; }

  .person-name {
    position: absolute;
    left: 40px;
    top: 186px;
    font-family: "Michroma", Arial, sans-serif;
    font-size: 17px;
    text-transform: uppercase;
    letter-spacing: 0.5px;
  }
  .person-name .first { color: var(--green); }
  .person-name .last { color: var(--navy); }

  .contact {
    position: absolute;
    left: 40px;
    top: 236px;
    display: flex;
    gap: 12px;
    font-size: 14px;
    color: var(--ink);
  }
  .contact .label { color: var(--navy); font-weight: 600; }
  .contact .sep { color: var(--ink); }

  .back-brand {
    position: absolute;
    left: 0; right: 0;
    top: 100px;
    display: flex;
    justify-content: center;
    align-items: center;
    gap: 12px;
    font-family: "Michroma", Arial, sans-serif;
    font-size: 24px;
    text-transform: uppercase;
  }
  .back-brand .brand-mark { width: 18px; height: 18px; background: #fff; }
  .website {
    position: absolute;
    left: 0; right: 0;
    top: 200px;
    text-align: center;
    font-family: "Michroma", Arial, sans-serif;
    font-size: 13px;
    letter-spacing: 1px;
    text-transform: uppercase;
  }
</style>
</head>
<body>
  <section class="card card-front">
    <div class="brand"><span class="brand-mark"></span><span>Corvath Build</span></div>
    <div class="rule rule-top"></div>
    <h1 class="person-name"><span class="first">Marisol</span> <span class="last">Brenkowitz</span></h1>
    <div class="rule rule-bottom"></div>
    <p class="contact">
      <span><span class="label">P:</span> 318-472-9051</span>
      <span class="sep">|</span>
      <span><span class="label">E:</span> corvathmb@mailvexo.com</span>
    </p>
  </section>

  <section class="card card-back">
    <div class="back-brand"><span class="brand-mark"></span><span>Corvath Build</span></div>
    <p class="website">www.corvathbuild.com</p>
  </section>
</body>
</html>
```